Premium Gold Vodka Label Design

English ------------------- We need a label for a Vodka Bottle. Its a sparkling premium vodka with gold inside. The design should look premium. We tried it on our selves but it looks horrible. Therefore we need your help. The current name is corvelle K, but we are open for any better suggestion. We attached the selfmade design. The label will be printed on the bottle. We have other design jobs for you (logo, other sorts)! English ------------------------ We need a label for a vodka bottle. This is a premium vodka which is offset with gold. The design should look like this. We have tried so far and failed. That is why we need your support. The name is so far corvelle K. If you have better suggestions we would be pleased about other suggestions / ideas. In the appendix the failed design is stored. The label is to be applied by screen printing. In the case of good work follow-up projects are guaranteed (logo, other varieties, etc)!
Updates

Reason: We need more time for the decision.

Target Market(s)

USA

Colors

Designer to choose colors to be used in the design.

Requirements
Must have
• English ------------------------ The needed text is on our selfmade label that is attached. English ------------------------ The required texts are stored in the attached design.
Nice to have
• English ------------------------ Transparent places are allowed because we want to print the label on the bottom. English ------------------------ As the label is applied by screen printing, transparent areas are also possible.

```html
<!DOCTYPE html>
<html lang="en">
<head>
<meta charset="UTF-8">
<title>Corvelle K Premium Gold Sparkling Vodka Label</title>
<link href="https://fonts.googleapis.com/css2?family=Tinos:wght@400;700&family=Cinzel:wght@700;900&family=Great+Vibes&display=swap" rel="stylesheet">
<style>
  :root {
    --bg: #f1f1f1;
    --gold-light: #fff3a6;
    --gold: #f2c230;
    --gold-deep: #c88a12;
    --gold-dark: #8f5a06;
    --ink: #111111;
    --red: #c4262b;
    --red-deep: #9e1a1f;
    --cream: #fde88a;
  }
  * { box-sizing: border-box; margin: 0; padding: 0; }
  html, body { width: 1200px; height: 980px; overflow: hidden; }
  body {
    background: var(--bg);
    position: relative;
    font-family: "Tinos", "Times New Roman", serif;
    color: var(--ink);
  }

  /* Main label */
  .main-label {
    position: absolute;
    left: 250px;
    top: 180px;
    width: 380px;
    height: 640px;
  }
  .main-label .frame { position: absolute; inset: 0; }
  .label-body { position: absolute; inset: 0; text-align: center; }

  .product-type {
    position: absolute; top: 70px; left: 0; right: 0;
    font-weight: 700; font-size: 48px; letter-spacing: 1px;
  }
  .product-line {
    position: absolute; top: 140px; left: 0; right: 0;
    font-weight: 700; font-size: 13px; letter-spacing: 0.3px;
  }
  .brand-band {
    position: absolute; top: 172px; left: 6px; right: 6px; height: 190px;
    background: linear-gradient(180deg, var(--red) 0%, var(--red-deep) 100%);
    box-shadow: 0 2px 0 var(--gold-deep), 0 -2px 0 var(--gold-deep);
  }
  .brand-mark {
    position: absolute; top: 210px; left: 0; right: 0;
    display: flex; justify-content: center; align-items: center; gap: 12px;
    font-family: "Cinzel", "Times New Roman", serif;
    font-weight: 900; font-size: 40px; color: var(--gold);
  }
  .brand-mark .mark-square {
    width: 22px; height: 22px; background: var(--gold);
  }
  .brand-name {
    position: absolute; top: 310px; left: 0; right: 0;
    font-family: "Cinzel", "Times New Roman", serif;
    font-weight: 700; font-size: 24px; letter-spacing: 2px; color: var(--gold);
  }
  .process {
    position: absolute; top: 430px; left: 0; right: 0;
    font-weight: 700; font-size: 15px; line-height: 1.35;
  }
  .process .accent { color: var(--red); font-size: 19px; }
  .strength {
    position: absolute; top: 508px; left: 62px; right: 62px;
    display: flex; justify-content: space-between;
    font-weight: 700; font-size: 12px;
  }
  .volume {
    position: absolute; top: 545px; left: 0; right: 0;
    font-weight: 700; font-size: 17px;
  }

  /* Neck label */
  .neck-label {
    position: absolute;
    left: 760px;
    top: 360px;
    width: 330px;
    height: 230px;
  }
  .neck-label .frame { position: absolute; inset: 0; }
  .neck-tagline {
    position: absolute; top: 44px; left: 0; right: 0; text-align: center;
    font-family: "Great Vibes", cursive;
    font-size: 24px; color: var(--gold-dark);
  }
  .neck-band {
    position: absolute; top: 84px; left: -4px; right: -4px; height: 58px;
    background: var(--red);
    border: 3px solid var(--gold);
    outline: 2px solid var(--red-deep);
    display: flex; align-items: center; justify-content: center;
    font-family: "Cinzel", "Times New Roman", serif;
    font-weight: 700; font-size: 28px; letter-spacing: 2px; color: #ffffff;
  }
  .neck-ornament {
    position: absolute; top: 152px; left: 115px; width: 100px; height: 10px;
    background: linear-gradient(90deg, transparent, var(--gold-deep), transparent);
  }
  .neck-year {
    position: absolute; top: 164px; left: 0; right: 0; text-align: center;
    font-family: "Cinzel", "Times New Roman", serif;
    font-weight: 700; font-size: 26px; color: var(--gold-dark);
  }
</style>
</head>
<body>

  <section class="main-label" aria-label="Main bottle label">
    <svg class="frame" viewBox="0 0 380 640" width="380" height="640" aria-hidden="true">
      <defs>
        <linearGradient id="goldRim" x1="0" y1="0" x2="1" y2="0">
          <stop offset="0" stop-color="#c88a12"/>
          <stop offset="0.25" stop-color="#fff3a6"/>
          <stop offset="0.5" stop-color="#f2c230"/>
          <stop offset="0.75" stop-color="#fff3a6"/>
          <stop offset="1" stop-color="#c88a12"/>
        </linearGradient>
        <radialGradient id="goldField" cx="0.5" cy="0.45" r="0.7">
          <stop offset="0" stop-color="#fff6b8"/>
          <stop offset="0.6" stop-color="#fde07a"/>
          <stop offset="1" stop-color="#e6ab2a"/>
        </radialGradient>
      </defs>
      <path d="M44 0 H336 A44 44 0 0 0 380 44 V596 A44 44 0 0 0 336 640 H44 A44 44 0 0 0 0 596 V44 A44 44 0 0 0 44 0 Z" fill="url(#goldRim)"/>
      <path d="M50 10 H330 A40 40 0 0 0 370 50 V590 A40 40 0 0 0 330 630 H50 A40 40 0 0 0 10 590 V50 A40 40 0 0 0 50 10 Z" fill="#111111"/>
      <path d="M56 22 H324 A34 34 0 0 0 358 56 V584 A34 34 0 0 0 324 618 H56 A34 34 0 0 0 22 584 V56 A34 34 0 0 0 56 22 Z" fill="url(#goldRim)"/>
      <path d="M60 28 H320 A32 32 0 0 0 352 60 V580 A32 32 0 0 0 320 612 H60 A32 32 0 0 0 28 580 V60 A32 32 0 0 0 60 28 Z" fill="url(#goldField)"/>
    </svg>
    <div class="label-body">
      <h1 class="product-type">VODKA</h1>
      <p class="product-line">PREMIUM GOLD SPARKLING</p>
      <div class="brand-band" role="img" aria-label="Red band with gold leaf pattern"></div>
      <div class="brand-mark"><span class="mark-square"></span><span>CORVELLE K</span></div>
      <p class="brand-name">CORVELLE K</p>
      <p class="process">Distilled <span class="accent">8</span> Filtered<br>Made in Germany</p>
      <p class="strength"><span>40%Alc Vol</span><span>80Proof</span></p>
      <p class="volume">200ml</p>
    </div>
  </section>

  <section class="neck-label" aria-label="Neck label">
    <svg class="frame" viewBox="0 0 330 230" width="330" height="230" aria-hidden="true">
      <defs>
        <linearGradient id="neckGold" x1="0" y1="0" x2="1" y2="1">
          <stop offset="0" stop-color="#fff3a6"/>
          <stop offset="0.5" stop-color="#f2c230"/>
          <stop offset="1" stop-color="#c88a12"/>
        </linearGradient>
      </defs>
      <path d="M60 0 H270 L330 45 V185 L270 230 H60 L0 185 V45 Z" fill="#c88a12"/>
      <path d="M64 8 H266 L322 49 V181 L266 222 H64 L8 181 V49 Z" fill="#111111"/>
      <path d="M68 14 H262 L316 53 V177 L262 216 H68 L14 177 V53 Z" fill="url(#neckGold)"/>
    </svg>
    <p class="neck-tagline">Premium Gold</p>
    <div class="neck-band">CORVELLE K</div>
    <div class="neck-ornament" role="img" aria-label="Gold flourish ornament"></div>
    <p class="neck-year">1974</p>
  </section>

</body>
</html>
```